Bluerock Data Partners - IT Support Tri-Fold

Need a tri-fold brochure for marketing, pitching managed IT Services. These services include computer/server management, security, cloud backups. The tri-fold should use our logo and colors (Attached)

```html
<!DOCTYPE html>
<html lang="en">
<head>
<meta charset="utf-8">
<title>Bluerock Data Partners – IT Support Tri-Fold</title>
<link rel="stylesheet" href="https://fonts.googleapis.com/css2?family=Exo+2:wght@500;600;700;800&family=Arimo:wght@400;700&display=swap">
<style>
  :root{
    --backdrop:#dcdcdc;
    --paper:#efefef;
    --paper-shade:#d9d9d9;
    --navy:#0e2740;
    --navy-deep:#0a1a2b;
    --blue:#1d6aa8;
    --blue-title:#1e5f9c;
    --red:#d50f2b;
    --red-dark:#a80b21;
    --green:#2aa068;
    --ink:#3b3b3b;
    --grey-title:#4a4a4a;
    --white:#ffffff;
  }
  *{margin:0;padding:0;box-sizing:border-box}
  html,body{width:846px;height:1200px;overflow:hidden}
  body{background:var(--backdrop);position:relative;font-family:"Arimo",Arial,sans-serif;color:var(--ink)}
  .spread{position:absolute;left:48px;width:750px;height:578px;overflow:hidden;background:var(--paper)}
  .spread--outside{top:15px}
  .spread--inside{top:607px}
  .spread-art{position:absolute;left:0;top:0;width:750px;height:578px}
  .panel{position:absolute;top:0;width:250px;height:578px}
  .panel--1{left:0}.panel--2{left:250px}.panel--3{left:500px}

  .heading{font-family:"Exo 2",sans-serif;font-weight:700;line-height:.95;text-transform:uppercase}
  .heading--services{position:absolute;left:17px;top:22px;font-size:23px}
  .heading--services .accent{color:var(--blue-title);display:block}
  .heading--services .base{color:var(--grey-title);display:block}
  .heading--business{position:absolute;right:20px;top:22px;font-size:23px;text-align:right}
  .heading--business .accent{color:var(--blue-title);display:block;font-size:17px}
  .heading--business .base{color:var(--grey-title);display:block}
  .heading--solutions{position:absolute;left:14px;top:22px;color:var(--white);font-size:23px}
  .heading--solutions .small{display:block;font-size:16px}

  .body-copy{font-size:8.3px;line-height:1.12;text-align:justify}
  .body-copy p+p{margin-top:9px}
  .copy--intro{position:absolute;left:17px;top:86px;width:216px}
  .copy--business{position:absolute;left:18px;top:86px;width:214px}

  .phone-line{position:absolute;left:42px;top:238px;display:flex;align-items:center;gap:10px}
  .phone-badge{width:26px;height:26px;border-radius:5px;background:var(--blue);display:flex;align-items:center;justify-content:center}
  .phone-number{font-family:"Exo 2",sans-serif;font-weight:700;font-size:20px;color:var(--blue-title)}

  .tagline{position:absolute;left:0;width:250px;top:82px;text-align:center;color:var(--white);font-family:"Exo 2",sans-serif;font-weight:600;font-size:8.8px;line-height:1.2}
  .solution-list{position:absolute;left:56px;top:118px;list-style:none;color:var(--white);font-family:"Exo 2",sans-serif;font-weight:600;font-size:7.6px;letter-spacing:.3px}
  .solution-list li{height:11.4px;display:flex;align-items:center;gap:5px}
  .tick{width:7px;height:7px;border:1px solid var(--white);border-radius:50%;display:inline-flex;align-items:center;justify-content:center;flex:none}

  .service-label{position:absolute;color:var(--white);font-family:"Exo 2",sans-serif;font-weight:700;text-align:center;line-height:1.05}
  .label--server{left:88px;top:268px;width:120px;font-size:8.6px}
  .label--security{left:20px;top:375px;width:80px;font-size:10.5px}
  .label--cloud{left:190px;top:448px;width:120px;font-size:12.5px}

  .panel--dark{background:var(--navy-deep)}
  .heading--why{position:absolute;left:23px;top:24px;color:var(--white);font-size:19px;font-weight:700}
  .heading--why .big{display:block;font-size:28px}
  .copy--why{position:absolute;left:18px;top:309px;width:214px;color:var(--white)}

  .web-button{position:absolute;top:531px;width:211px;height:26px;border:1.5px solid currentColor;display:flex;align-items:center;justify-content:center;font-family:"Exo 2",sans-serif;font-weight:600;font-size:10.5px;letter-spacing:.2px}
  .web-button--dark{left:16px;color:var(--white)}
  .web-button--light{left:20px;color:var(--navy)}

  .contact-title{position:absolute;left:46px;top:405px;color:var(--blue-title);font-family:"Exo 2",sans-serif;font-weight:700;font-size:12px}
  .contact-list{position:absolute;left:62px;top:437px;list-style:none;font-size:7.4px;color:var(--ink)}
  .contact-list li{display:flex;align-items:center;gap:9px;height:27px;line-height:1.1}
  .contact-dot{width:16px;height:16px;border-radius:50%;flex:none;display:flex;align-items:center;justify-content:center}
  .dot--red{background:var(--red)}.dot--green{background:var(--green)}.dot--blue{background:var(--blue)}

  .brand{position:absolute;left:0;width:250px;top:478px;display:flex;align-items:center;justify-content:center;gap:7px}
  .brand-square{width:14px;height:14px;background:var(--blue)}
  .brand-name{font-family:"Exo 2",sans-serif;font-weight:700;font-size:13.5px;color:var(--navy)}
</style>
</head>
<body>

<!-- Outside spread -->
<section class="spread spread--outside">
  <svg class="spread-art" viewBox="0 0 750 578" xmlns="http://www.w3.org/2000/svg">
    <defs>
      <linearGradient id="paperFade" x1="0" x2="1"><stop offset="0" stop-color="#f2f2f2"/><stop offset=".85" stop-color="#e8e8e8"/><stop offset="1" stop-color="#d6d6d6"/></linearGradient>
      <linearGradient id="serverRoom" x1="0" y1="0" x2="0" y2="1"><stop offset="0" stop-color="#2c3742"/><stop offset=".5" stop-color="#161c24"/><stop offset="1" stop-color="#3b434b"/></linearGradient>
      <linearGradient id="blueRoom" x1="0" y1="0" x2="1" y2="1"><stop offset="0" stop-color="#1b4b6b"/><stop offset=".6" stop-color="#2a6688"/><stop offset="1" stop-color="#163a55"/></linearGradient>
      <linearGradient id="techRoom" x1="0" y1="0" x2="1" y2="0"><stop offset="0" stop-color="#3c4550"/><stop offset=".5" stop-color="#c9ccd0"/><stop offset="1" stop-color="#2a3038"/></linearGradient>
    </defs>
    <rect class="panel-bg" x="0" y="0" width="250" height="578" fill="url(#paperFade)"/>
    <rect class="panel-bg" x="250" y="0" width="250" height="578" fill="#ededed"/>
    <rect class="photo photo--solutions" x="500" y="0" width="250" height="330" fill="url(#blueRoom)" role="img" aria-label="Photo of a data centre aisle lined with server racks, blue tone"/>
    <rect class="photo photo--racks" x="250" y="280" width="250" height="298" fill="url(#serverRoom)" role="img" aria-label="Photo of server racks in a data centre"/>
    <rect class="photo photo--technician" x="500" y="280" width="250" height="298" fill="url(#techRoom)" role="img" aria-label="Photo of a technician working at a server rack"/>
    <polygon class="chevron-band" points="250,270 500,338 750,270 750,290 500,360 250,290" fill="var(--red)"/>
    <polygon class="chevron-band" points="280,270 500,330 750,262 750,270 500,338 250,270" fill="#ededed"/>
    <polygon points="500,262 750,262 750,270 500,338" fill="url(#blueRoom)"/>
    <line x1="250" y1="0" x2="250" y2="578" stroke="#c8c8c8" stroke-width="1"/>
    <line x1="500" y1="0" x2="500" y2="578" stroke="#c8c8c8" stroke-width="1"/>

    <g class="diamonds">
      <polygon points="229,186 251,208 229,230 207,208" fill="var(--red)"/>
      <polygon points="193,525 215,547 193,569 171,547" fill="var(--blue)"/>
      <polygon points="57,233 157,333 57,433 -43,333" fill="var(--blue)"/>
      <polygon points="120,420 195,495 120,570 45,495" fill="var(--green)"/>
      <polygon points="148,177 226,255 148,333 70,255" fill="var(--navy)"/>
      <polygon points="250,277 395,422 250,567 105,422" fill="var(--red)"/>
    </g>

    <g class="service-icons">
      <circle cx="148" cy="225" r="27" fill="var(--white)"/>
      <rect x="138" y="208" width="20" height="32" rx="2" fill="var(--navy)"/>
      <rect x="142" y="213" width="12" height="2" fill="var(--white)"/>
      <rect x="142" y="218" width="12" height="2" fill="var(--white)"/>
      <circle cx="148" cy="233" r="2" fill="var(--white)"/>

      <circle cx="60" cy="335" r="35" fill="var(--white)"/>
      <path d="M60 315 L76 321 V334 C76 345 69 352 60 356 C51 352 44 345 44 334 V321 Z" fill="none" stroke="var(--blue)" stroke-width="3"/>
      <rect x="53" y="333" width="14" height="11" rx="1.5" fill="var(--blue)"/>
      <path d="M56 333 V329 a4 4 0 0 1 8 0 V333" fill="none" stroke="var(--blue)" stroke-width="2"/>

      <circle cx="250" cy="396" r="32" fill="var(--white)"/>
      <path d="M234 404 a8 8 0 0 1 2 -15 a12 12 0 0 1 23 -2 a9 9 0 0 1 6 17 Z" fill="none" stroke="var(--red)" stroke-width="3.2" stroke-linejoin="round"/>
      <path d="M243 396 a6 6 0 0 1 12 0 a6 6 0 0 1 -12 0" fill="none" stroke="var(--red)" stroke-width="3"/>
    </g>
  </svg>

  <div class="panel panel--1">
    <h1 class="heading heading--services"><span class="accent">BDP IT</span><span class="base">Services</span></h1>
    <div class="body-copy copy--intro">
      <p>We've got the experience and knowledge to solve your business tech needs. We have been serving residents of CT &amp; RI since 2015, and have strived to make the world of technology easier and less stressful for our clients.</p>
    </div>
    <div class="service-label label--server">Computer<br>Server Management</div>
    <div class="service-label label--security">Security</div>
    <div class="service-label label--cloud">Cloud Backups</div>
  </div>

  <div class="panel panel--2">
    <h2 class="heading heading--business"><span class="accent">Business</span><span class="base">Services</span></h2>
    <div class="body-copy copy--business">
      <p>BDP aims to help small businesses thrive by managing the technical aspects so they can focus on what they do best. We offer various services and are happy to travel on-site to CT, RI and MA to provide them. Our premier business service is managed IT, one multiple businesses within the RI area have subscribed to to keep everything working flawlessly.</p>
      <p>Feel free to schedule with us or to inquire about services through our Contact Us button or Phone number provided, or select a service below to schedule through our online booking system. Alternatively, you may book directly from any service page by clicking on the corresponding icon below.</p>
    </div>
    <div class="phone-line">
      <span class="phone-badge">
        <svg width="16" height="16" viewBox="0 0 24 24"><path d="M6.6 10.8a15.1 15.1 0 0 0 6.6 6.6l2.2-2.2a1 1 0 0 1 1-.25 11.4 11.4 0 0 0 3.6.57 1 1 0 0 1 1 1V20a1 1 0 0 1-1 1A17 17 0 0 1 3 4a1 1 0 0 1 1-1h3.5a1 1 0 0 1 1 1c0 1.25.2 2.45.57 3.57a1 1 0 0 1-.25 1z" fill="#fff"/></svg>
      </span>
      <span class="phone-number">401-555-0182</span>
    </div>
  </div>

  <div class="panel panel--3">
    <h2 class="heading heading--solutions"><span class="small">Our</span>Solutions</h2>
    <p class="tagline">Bluerock Data Partners, Delivering Success<br>with Every Solution.</p>
    <ul class="solution-list">
      <li><span class="tick"><svg width="5" height="5" viewBox="0 0 10 10"><path d="M1 5l3 3 5-6" stroke="#fff" stroke-width="2" fill="none"/></svg></span>Email setup</li>
      <li><span class="tick"><svg width="5" height="5" viewBox="0 0 10 10"><path d="M1 5l3 3 5-6" stroke="#fff" stroke-width="2" fill="none"/></svg></span>Virus removal</li>
      <li><span class="tick"><svg width="5" height="5" viewBox="0 0 10 10"><path d="M1 5l3 3 5-6" stroke="#fff" stroke-width="2" fill="none"/></svg></span>Tune up</li>
      <li><span class="tick"><svg width="5" height="5" viewBox="0 0 10 10"><path d="M1 5l3 3 5-6" stroke="#fff" stroke-width="2" fill="none"/></svg></span>Computer setup</li>
      <li><span class="tick"><svg width="5" height="5" viewBox="0 0 10 10"><path d="M1 5l3 3 5-6" stroke="#fff" stroke-width="2" fill="none"/></svg></span>Data backup</li>
      <li><span class="tick"><svg width="5" height="5" viewBox="0 0 10 10"><path d="M1 5l3 3 5-6" stroke="#fff" stroke-width="2" fill="none"/></svg></span>Printer setup</li>
      <li><span class="tick"><svg width="5" height="5" viewBox="0 0 10 10"><path d="M1 5l3 3 5-6" stroke="#fff" stroke-width="2" fill="none"/></svg></span>Data recovery</li>
      <li><span class="tick"><svg width="5" height="5" viewBox="0 0 10 10"><path d="M1 5l3 3 5-6" stroke="#fff" stroke-width="2" fill="none"/></svg></span>Phone setup &amp; configuration</li>
      <li><span class="tick"><svg width="5" height="5" viewBox="0 0 10 10"><path d="M1 5l3 3 5-6" stroke="#fff" stroke-width="2" fill="none"/></svg></span>Software install</li>
      <li><span class="tick"><svg width="5" height="5" viewBox="0 0 10 10"><path d="M1 5l3 3 5-6" stroke="#fff" stroke-width="2" fill="none"/></svg></span>Managed it services</li>
      <li><span class="tick"><svg width="5" height="5" viewBox="0 0 10 10"><path d="M1 5l3 3 5-6" stroke="#fff" stroke-width="2" fill="none"/></svg></span>On-site troubleshooting</li>
      <li><span class="tick"><svg width="5" height="5" viewBox="0 0 10 10"><path d="M1 5l3 3 5-6" stroke="#fff" stroke-width="2" fill="none"/></svg></span>Graphic design</li>
      <li><span class="tick"><svg width="5" height="5" viewBox="0 0 10 10"><path d="M1 5l3 3 5-6" stroke="#fff" stroke-width="2" fill="none"/></svg></span>Server configuration</li>
      <li><span class="tick"><svg width="5" height="5" viewBox="0 0 10 10"><path d="M1 5l3 3 5-6" stroke="#fff" stroke-width="2" fill="none"/></svg></span>Wifi/wired network install &amp; setup</li>
    </ul>
  </div>
</section>

<!-- Inside spread -->
<section class="spread spread--inside">
  <svg class="spread-art" viewBox="0 0 750 578" xmlns="http://www.w3.org/2000/svg">
    <defs>
      <linearGradient id="paperRight" x1="0" x2="1"><stop offset="0" stop-color="#e4e4e4"/><stop offset=".35" stop-color="#f3f3f3"/><stop offset="1" stop-color="#e6e6e6"/></linearGradient>
      <linearGradient id="engineerPhoto" x1="0" y1="0" x2="1" y2="1"><stop offset="0" stop-color="#3a4754"/><stop offset=".5" stop-color="#1a232d"/><stop offset="1" stop-color="#5c6874"/></linearGradient>
      <linearGradient id="tabletPhoto" x1="0" y1="0" x2="1" y2="1"><stop offset="0" stop-color="#dfe6ec"/><stop offset=".5" stop-color="#b8c4cf"/><stop offset="1" stop-color="#8a9aa8"/></linearGradient>
      <linearGradient id="redPhoto" x1="0" y1="0" x2="1" y2="1"><stop offset="0" stop-color="#d50f2b"/><stop offset="1" stop-color="#8c0a1c"/></linearGradient>
    </defs>
    <rect x="0" y="0" width="250" height="578" fill="var(--navy-deep)"/>
    <rect x="250" y="0" width="500" height="578" fill="url(#paperRight)"/>
    <rect class="photo photo--engineer" x="0" y="120" width="245" height="173" fill="url(#engineerPhoto)" role="img" aria-label="Photo of an engineer with a laptop in a dim server room"/>
    <line x1="500" y1="0" x2="500" y2="578" stroke="#cfcfcf" stroke-width="1"/>

    <g class="diamonds">
      <polygon points="422,-10 482,50 422,110 362,50" fill="var(--blue)"/>
      <polygon points="682,-36 742,24 682,84 622,24" fill="var(--green)"/>
      <polygon points="630,-10 690,50 630,110 570,50" fill="var(--blue)"/>
      <polygon points="760,40 810,90 760,140 710,90" fill="var(--red)"/>
      <polygon points="344,49 434,139 344,229 254,139" fill="var(--navy)"/>
      <polygon points="662,87 792,217 662,347 532,217" fill="url(#redPhoto)" role="img" aria-label="Red-toned photo of hands typing on a laptop"/>
      <polygon points="479,170 609,300 479,430 349,300" fill="var(--green)"/>
      <polygon points="578,308 648,378 578,448 508,378" fill="var(--blue)"/>
      <polygon points="500,24 630,154 500,284 370,154" fill="url(#tabletPhoto)" role="img" aria-label="Photo of hands holding a tablet showing business charts"/>
    </g>
  </svg>

  <div class="panel panel--1">
    <h2 class="heading heading--why">Why People<br>Choose<span class="big">Us</span></h2>
    <div class="body-copy copy--why">
      <p>Since 2015, Bluerock Data Partners has provided Southern New England with on-site, and remote technical support services. We primarily serve eastern Connecticut, Rhode Island, and Southern Massachusetts.</p>
      <p>We pride ourselves on industry-leading response time, with a focus on customer service. When you call our office, a real representative in Connecticut will answer, not an outsourced answering system.</p>
      <p>With over 30 years of combined experience across our team, we work to provide real solutions to you – whether you need help fixing your home's computer, need one hundred computers upgraded for your business, or are looking to build a website – we will explain the technology to you in a language you understand, and provide a personalized solution for your unique situation.</p>
    </div>
    <div class="web-button web-button--dark">WWW.BLUEROCKDATA.EXAMPLE</div>
  </div>

  <div class="panel panel--2">
    <h3 class="contact-title">GET IN TOUCH WITH US</h3>
    <ul class="contact-list">
      <li><span class="contact-dot dot--red"><svg width="8" height="8" viewBox="0 0 24 24"><path d="M6.6 10.8a15.1 15.1 0 0 0 6.6 6.6l2.2-2.2a1 1 0 0 1 1-.25 11.4 11.4 0 0 0 3.6.57 1 1 0 0 1 1 1V20a1 1 0 0 1-1 1A17 17 0 0 1 3 4a1 1 0 0 1 1-1h3.5a1 1 0 0 1 1 1c0 1.25.2 2.45.57 3.57a1 1 0 0 1-.25 1z" fill="#fff"/></svg></span>+1 401-555-0182</li>
      <li><span class="contact-dot dot--green"><svg width="8" height="8" viewBox="0 0 24 24"><rect x="2" y="5" width="20" height="14" rx="2" fill="#fff"/><path d="M2 6l10 7 10-7" stroke="#2aa068" stroke-width="2" fill="none"/></svg></span>hello@bluerockdata.example</li>
      <li><span class="contact-dot dot--blue"><svg width="8" height="8" viewBox="0 0 24 24"><path d="M12 2a7 7 0 0 0-7 7c0 5 7 13 7 13s7-8 7-13a7 7 0 0 0-7-7zm0 9.5a2.5 2.5 0 1 1 0-5 2.5 2.5 0 0 1 0 5z" fill="#fff"/></svg></span>27 Mill Pond Road,<br>Stonington CT 06378</li>
    </ul>
    <div class="web-button web-button--light">WWW.BLUEROCKDATA.EXAMPLE</div>
  </div>

  <div class="panel panel--3">
    <div class="brand">
      <span class="brand-square"></span>
      <span class="brand-name">Bluerock Data Partners</span>
    </div>
    <div class="web-button web-button--light">WWW.BLUEROCKDATA.EXAMPLE</div>
  </div>
</section>

</body>
</html>
```